We need visit card and a letter paper for our website. thx

We have a beauty clinic in Switzerland.
https://wolkenbachtal.ch
We need a visit card.

Requirements
Must have
• see colors on website

```html
<!DOCTYPE html>
<html lang="en">
<head>
<meta charset="utf-8">
<title>Wolkenbachtal Beauty Clinic – Stationery</title>
<link href="https://fonts.googleapis.com/css2?family=Josefin+Sans:wght@300;400;600&display=swap" rel="stylesheet">
<style>
  :root {
    --bg: #ececee;
    --card: #f7f7f8;
    --berry: #a4406c;
    --ink: #1c1c1e;
    --grey: #7b7b80;
    --rule: #8f8f94;
  }
  * { margin: 0; padding: 0; box-sizing: border-box; }
  html, body { width: 1200px; height: 720px; overflow: hidden; background: var(--bg); }
  body { font-family: "Josefin Sans", sans-serif; position: relative; }

  .card {
    position: absolute; top: 205px; width: 520px; height: 300px;
    background: var(--card); box-shadow: 0 2px 10px rgba(0,0,0,.08); overflow: hidden;
  }
  .card--contact { left: 40px; }
  .card--reminder { left: 640px; }

  .brand-name { font-weight: 400; color: var(--ink); letter-spacing: .5px; }

  /* contact card */
  .card--contact .brand-name { position: absolute; left: 36px; top: 138px; font-size: 30px; }
  .contact { position: absolute; left: 278px; top: 48px; width: 220px; }
  .contact__name { color: var(--berry); font-size: 19px; font-weight: 400; letter-spacing: .5px; }
  .contact__rule { height: 1px; background: var(--rule); margin: 12px 0 18px; }
  .contact__address, .contact__line { color: var(--grey); font-size: 13px; font-weight: 300; line-height: 1.5; }
  .contact__list { list-style: none; margin-top: 18px; }
  .contact__line { display: flex; align-items: center; gap: 8px; margin-bottom: 3px; }
  .contact__icon { width: 14px; height: 14px; flex: none; }

  /* reminder card */
  .card--reminder .brand-name { position: absolute; right: 30px; top: 26px; font-size: 22px; }
  .reminder__title {
    position: absolute; left: 30px; top: 70px; color: var(--berry);
    font-size: 14px; letter-spacing: 3px; font-weight: 400;
  }
  .field {
    position: absolute; left: 30px; right: 30px; height: 24px;
    border-bottom: 1px solid var(--berry); font-size: 11px; letter-spacing: 2.5px; color: var(--grey);
    display: flex; align-items: flex-end; padding-bottom: 3px;
  }
  .field--name { top: 98px; }
  .field--name .field__time { margin-left: auto; margin-right: 80px; }
  .field--date { top: 128px; }
  .field--purpose { top: 158px; }
  .days { position: absolute; left: 30px; top: 196px; display: flex; gap: 14px; list-style: none; }
  .day { display: flex; align-items: center; gap: 7px; font-size: 11px; letter-spacing: 2px; color: var(--grey); }
  .day__box { width: 18px; height: 18px; border: 1px solid var(--berry); }
  .reminder__address {
    position: absolute; left: 30px; top: 232px; font-size: 11px; color: var(--grey);
    letter-spacing: .8px; display: flex; align-items: center; gap: 10px;
  }
  .reminder__phone { display: flex; align-items: center; gap: 5px; }
  .reminder__band-rule { position: absolute; left: 0; right: 0; bottom: 38px; height: 2px; background: #b5b5ba; }
  .reminder__band {
    position: absolute; left: 0; right: 0; bottom: 0; height: 34px; background: var(--berry);
    color: #f3dbe5; font-size: 10px; font-weight: 300; letter-spacing: .6px; line-height: 1.35;
    display: flex; align-items: center; justify-content: center; text-align: center; padding: 0 24px;
  }
</style>
</head>
<body>

<section class="card card--contact">
  <div class="brand-name">Wolkenbachtal</div>
  <div class="contact">
    <h1 class="contact__name">Dr. Lena Hofer</h1>
    <div class="contact__rule"></div>
    <p class="contact__address">Bergweg 4,<br>7560 Talwil, Switzerland</p>
    <ul class="contact__list">
      <li class="contact__line">
        <svg class="contact__icon" viewBox="0 0 14 14"><circle cx="7" cy="7" r="7" fill="#a4406c"/><path d="M4.3 4.2c.4-.4.9-.4 1.1 0l.6 1c.2.3.1.6-.1.8l-.4.3c.4.8 1 1.4 1.8 1.8l.3-.4c.2-.2.5-.3.8-.1l1 .6c.4.2.4.7 0 1.1-.5.5-1.1.7-1.8.4C6.1 9 5 7.9 4.4 6.4c-.3-.7-.6-1.6-.1-2.2z" fill="#fff"/></svg>
        +41 (0) 800 24 30 50
      </li>
      <li class="contact__line">
        <svg class="contact__icon" viewBox="0 0 14 14"><circle cx="7" cy="7" r="7" fill="#a4406c"/><rect x="3.7" y="4.8" width="6.6" height="4.6" fill="none" stroke="#fff" stroke-width=".9"/><path d="M3.8 5l3.2 2.4L10.2 5" fill="none" stroke="#fff" stroke-width=".9"/></svg>
        hallo@wolkenbachtal.ch
      </li>
      <li class="contact__line">
        <svg class="contact__icon" viewBox="0 0 14 14"><circle cx="7" cy="7" r="7" fill="#a4406c"/><circle cx="7" cy="7" r="3.3" fill="none" stroke="#fff" stroke-width=".9"/><path d="M3.7 7h6.6M7 3.7c-1.4 1.8-1.4 4.8 0 6.6M7 3.7c1.4 1.8 1.4 4.8 0 6.6" fill="none" stroke="#fff" stroke-width=".7"/></svg>
        wolkenbachtal.ch
      </li>
    </ul>
  </div>
</section>

<section class="card card--reminder">
  <div class="brand-name">Wolkenbachtal</div>
  <h2 class="reminder__title">Appointment Reminder</h2>
  <div class="field field--name"><span>Patient`s Name:</span><span class="field__time">Time:</span></div>
  <div class="field field--date"><span>Date:</span></div>
  <div class="field field--purpose"><span>Purpose:</span></div>
  <ul class="days">
    <li class="day"><span>Mon</span><span class="day__box"></span></li>
    <li class="day"><span>Tues</span><span class="day__box"></span></li>
    <li class="day"><span>Wed</span><span class="day__box"></span></li>
    <li class="day"><span>Thur</span><span class="day__box"></span></li>
    <li class="day"><span>Fri</span><span class="day__box"></span></li>
  </ul>
  <div class="reminder__address">
    <span>7560 Talwil, Switzerland</span>
    <span class="reminder__phone">
      <svg width="10" height="10" viewBox="0 0 14 14"><path d="M2.3 1.5c.6-.6 1.3-.6 1.6 0l1 1.6c.3.5.2.9-.2 1.2l-.6.5c.6 1.3 1.6 2.3 2.9 2.9l.5-.6c.3-.4.7-.5 1.2-.2l1.6 1c.6.3.6 1 0 1.6-.8.8-1.8 1.1-2.9.6C5 9.1 3.3 7.4 2.4 5.1 1.9 4 1.5 2.4 2.3 1.5z" fill="#a4406c"/></svg>
      +41 (0) 800 24 30 50
    </span>
  </div>
  <div class="reminder__band-rule"></div>
  <p class="reminder__band">Please respect your time and that of other guests and give a 24 hr notice if you are not able to keep your appointment.</p>
</section>

</body>
</html>
```